R. Tanford Realty, Inc business card (2 sided), letterhead (1 sided) & #10 envelope (1 sided)

business card of standard size utilizing the attached logo. Side one with logo, Wade Tanford (my name), President / Broker (title), 707-555-0183 (phone), www.rtanfordrealty.example (website), 1726 Pelham Avenue, Suite 4403 Cedar Hollow, CA 95999 (business address) wade.rtanfordrealty@mailbox.example (e-mail address),
Side two - Log

Letterhead and #10 envelope in the same theme

Project Deadline Extended
Reason: I think a 2 day deadline may be a bit ambitious on my part. I have extended the deadline to 4 days. Thanks!

```html
<!DOCTYPE html>
<html lang="en">
<head>
<meta charset="utf-8">
<title>R. Tanford Realty, Inc — Business Card</title>
<link rel="stylesheet" href="https://fonts.googleapis.com/css2?family=Didact+Gothic&family=Montserrat:wght@400;600&display=swap">
<style>
  :root {
    --blue-deep: #1683c2;
    --blue: #2196d3;
    --blue-light: #45ade0;
    --white: #ffffff;
    --grey: #6d6e71;
    --ink: #4a4b4d;
    --backdrop: #e8e6e2;
  }
  * { box-sizing: border-box; margin: 0; padding: 0; }
  html, body { width: 1200px; height: 1184px; overflow: hidden; }
  body {
    background: var(--backdrop);
    font-family: "Didact Gothic", "Century Gothic", sans-serif;
    position: relative;
  }
  .card {
    position: absolute;
    left: 150px;
    width: 900px;
    height: 514px;
    overflow: hidden;
    box-shadow: 0 6px 18px rgba(0,0,0,.18);
  }
  .card--front { top: 52px; background: linear-gradient(120deg, var(--blue-deep) 0%, var(--blue) 55%, var(--blue-light) 100%); }
  .card--back { top: 616px; background: var(--white); }

  /* front */
  .brand {
    position: absolute;
    left: 0; right: 0; top: 170px;
    display: flex; align-items: center; justify-content: center; gap: 22px;
    font-family: "Montserrat", sans-serif;
    font-weight: 400;
    font-size: 58px;
    color: var(--white);
  }
  .brand__mark { width: 30px; height: 30px; background: var(--white); flex: none; }
  .front-web {
    position: absolute; left: 0; right: 0; top: 300px;
    text-align: center; color: var(--white);
    font-size: 22px; letter-spacing: 6px;
  }

  /* back */
  .wave { position: absolute; inset: 0; width: 900px; height: 514px; }
  .brand--small {
    top: 92px; left: 50px; right: auto;
    justify-content: flex-start; gap: 12px;
    font-size: 30px; color: var(--blue-deep);
  }
  .brand--small .brand__mark { width: 16px; height: 16px; background: var(--blue-deep); }
  .contact {
    position: absolute; left: 470px; top: 62px;
    list-style: none; color: var(--ink); font-size: 19px; line-height: 1.3;
  }
  .contact li { display: flex; align-items: flex-start; gap: 12px; margin-bottom: 9px; }
  .contact li.gap { margin-bottom: 26px; }
  .contact svg { width: 16px; height: 16px; flex: none; margin-top: 3px; fill: var(--blue-deep); }
  .person { position: absolute; left: 58px; top: 384px; color: var(--white); }
  .person__name {
    font-family: "Montserrat", sans-serif; font-weight: 600;
    font-size: 40px; letter-spacing: -1px; text-transform: uppercase;
  }
  .person__name .surname { color: var(--grey); }
  .person__title { font-size: 24px; letter-spacing: 9px; margin-top: 2px; padding-left: 34px; }
</style>
</head>
<body>

<section class="card card--front" aria-label="Card front">
  <div class="brand"><span class="brand__mark"></span>R. Tanford Realty, Inc</div>
  <p class="front-web">www.rtanfordrealty.example</p>
</section>

<section class="card card--back" aria-label="Card back">
  <svg class="wave" viewBox="0 0 900 514" aria-hidden="true">
    <defs>
      <linearGradient id="bandFill" x1="0" y1="0" x2="1" y2="1">
        <stop offset="0" stop-color="#1683c2"/>
        <stop offset="1" stop-color="#45ade0"/>
      </linearGradient>
    </defs>
    <path d="M0 318 C190 236 360 232 480 282 C610 336 740 346 900 280" fill="none" stroke="#1683c2" stroke-width="3"/>
    <path d="M0 340 C190 262 360 256 480 304 C610 358 740 368 900 300 L900 514 L0 514 Z" fill="url(#bandFill)"/>
    <path d="M0 362 C190 286 360 280 480 326 C610 378 740 386 900 322" fill="none" stroke="#ffffff" stroke-width="4"/>
  </svg>

  <div class="brand brand--small"><span class="brand__mark"></span>R. Tanford Realty, Inc</div>

  <ul class="contact">
    <li class="gap">
      <svg viewBox="0 0 16 16"><path d="M8 0a5.5 5.5 0 0 0-5.5 5.5C2.5 10 8 16 8 16s5.5-6 5.5-10.5A5.5 5.5 0 0 0 8 0zm0 8a2.5 2.5 0 1 1 0-5 2.5 2.5 0 0 1 0 5z"/></svg>
      <span>1726 Pelham Avenue,<br>Suite 4403 Cedar Hollow, CA 95999</span>
    </li>
    <li>
      <svg viewBox="0 0 16 16"><path d="M4 0h8a1 1 0 0 1 1 1v14a1 1 0 0 1-1 1H4a1 1 0 0 1-1-1V1a1 1 0 0 1 1-1zm1 2v10h6V2H5zm3 11a1 1 0 1 0 0 2 1 1 0 0 0 0-2z"/></svg>
      <span>707-555-0183</span>
    </li>
    <li>
      <svg viewBox="0 0 16 16"><path d="M0 3h16v10H0V3zm1.5 1.2L8 9l6.5-4.8V4h-13v.2z"/></svg>
      <span>wade.rtanfordrealty@mailbox.example</span>
    </li>
    <li>
      <svg viewBox="0 0 16 16"><path d="M8 0a8 8 0 1 0 0 16A8 8 0 0 0 8 0zm5.9 7h-2.5a12 12 0 0 0-1-4.6A6 6 0 0 1 13.9 7zM8 2c.8 1 1.4 2.8 1.5 5h-3C6.6 4.8 7.2 3 8 2zM5.6 2.4A12 12 0 0 0 4.6 7H2.1a6 6 0 0 1 3.5-4.6zM2.1 9h2.5a12 12 0 0 0 1 4.6A6 6 0 0 1 2.1 9zM8 14c-.8-1-1.4-2.8-1.5-5h3c-.1 2.2-.7 4-1.5 5zm2.4-.4a12 12 0 0 0 1-4.6h2.5a6 6 0 0 1-3.5 4.6z"/></svg>
      <span>www.rtanfordrealty.example</span>
    </li>
  </ul>

  <div class="person">
    <p class="person__name">Wade<span class="surname">Tanford</span></p>
    <p class="person__title">BROKER</p>
  </div>
</section>

</body>
</html>
```